International business needs business cards

Our company, RUV Partners Inc. is in the business of supplying a range construction products with particular emphasis on CEMENT. We have developed our own brand - BOREAL SUPPLIES - with which to infiltrate the market. We are launching our brand of cement (BOREAL Type IS Cement) into the Caribbean which is unlike anything this market has ever seen. A monopoly has existed here for the past 60-odd years and the market has now opened to allow the importation of other brands and consumers are anxious and ready for change/improvement. We are very excited to be launching and want to make a great first impression. We will be conducting workshops and seminars (from government level to the hardware store owners) and we want our business card to give us the strong, confident introduction that we need.

Target Market(s)

construction; builders; engineers; home owners

Industry/Entity Type

Construction

Contact Information for Business Card

Melvina Tosh
CEO
cell # 1 868 5550147
Ground floor,Palmetto Plaza Suite 2473
George Town,Grand Cayman
Cayman Islands,KY1-1990
EMAIL: m.tosh@ruvpartnersinc.example
web site ruvpartnersinc.example

COMPANY: skype info ruv.partners.example

second card
Hester Quimby-Tosh
CFO
CELL# 1 868 555 0382
George Town,Grand Cayman
Cayman Islands,KY1-1990
EMAIL: h.quimbytosh@ruvpartnersinc.example
website ruvpartnersinc.example

Requirements
Must have
• Business cards must display BOTH logos - RUV is the company and BOREAL SUPPLIES is the brand.

```html
<!DOCTYPE html>
<html lang="en">
<head>
<meta charset="utf-8">
<title>RUV Partners Inc. — Business Card</title>
<link rel="stylesheet" href="https://fonts.googleapis.com/css2?family=Open+Sans:wght@400;600;700&display=swap">
<style>
  :root {
    --backdrop: #3a3532;
    --card: #111111;
    --card-edge: #1c1c1c;
    --accent: #ec7a22;
    --maroon: #7e1f1f;
    --text: #f2f2f2;
    --muted: #bdbdbd;
    --silver: #d6d6d6;
    --rule: #5a5a5a;
  }
  * { margin: 0; padding: 0; box-sizing: border-box; }
  html, body { width: 1200px; height: 814px; overflow: hidden; }
  body {
    background: var(--backdrop);
    font-family: "Open Sans", Arial, sans-serif;
    position: relative;
  }
  .card {
    position: absolute;
    top: 257px;
    width: 525px;
    height: 300px;
    background: var(--card);
    border: 1px solid var(--card-edge);
    box-shadow: 0 10px 26px rgba(0,0,0,0.45);
  }
  .card--front { left: 60px; }
  .card--back { left: 615px; }

  /* Front */
  .company-mark {
    position: absolute;
    left: 34px;
    top: 150px;
    display: flex;
    align-items: center;
    gap: 12px;
  }
  .company-mark__square {
    width: 62px; height: 62px;
    background: var(--maroon);
  }
  .company-mark__name {
    color: var(--text);
    font-weight: 700;
    font-size: 21px;
    line-height: 1.1;
  }
  .divider {
    position: absolute;
    left: 262px;
    top: 38px;
    width: 1px;
    height: 224px;
    background: linear-gradient(to bottom, transparent, var(--rule) 20%, var(--rule) 80%, transparent);
  }
  .contact {
    position: absolute;
    left: 282px;
    top: 46px;
    color: var(--text);
    font-size: 12.5px;
    line-height: 1.35;
  }
  .contact__name {
    color: var(--accent);
    font-weight: 600;
    font-size: 17px;
    line-height: 1.2;
  }
  .contact__title { margin-bottom: 10px; }
  .contact__address { margin-bottom: 12px; }
  .contact__row {
    display: flex;
    align-items: center;
    gap: 9px;
    margin-bottom: 3px;
  }
  .contact__row svg { width: 12px; height: 12px; flex: none; }

  /* Back */
  .brand-row {
    position: absolute;
    left: 48px;
    top: 92px;
    display: flex;
    align-items: center;
    gap: 40px;
  }
  .brand-mark, .company-mark--silver {
    display: flex;
    align-items: center;
    gap: 10px;
  }
  .brand-mark__circle {
    width: 58px; height: 58px;
    border-radius: 50%;
    background: var(--silver);
  }
  .brand-mark__name, .company-mark--silver .company-mark__name {
    color: var(--silver);
    font-weight: 700;
    font-size: 19px;
    line-height: 1.1;
  }
  .company-mark--silver .company-mark__square {
    width: 52px; height: 52px;
    background: var(--silver);
  }
  .website {
    position: absolute;
    right: 56px;
    top: 208px;
    color: var(--muted);
    font-size: 12px;
    letter-spacing: 2px;
  }
</style>
</head>
<body>
  <section class="card card--front">
    <div class="company-mark">
      <div class="company-mark__square"></div>
      <div class="company-mark__name">RUV Partners<br>Inc.</div>
    </div>
    <div class="divider"></div>
    <div class="contact">
      <p class="contact__name">Melvina Tosh</p>
      <p class="contact__title">CEO</p>
      <p class="contact__address">Ground floor<br>Palmetto Plaza Suite 2473<br>George Town,Grand Cayman<br>Cayman Islands,KY1-1990</p>
      <p class="contact__row">
        <svg viewBox="0 0 12 12" aria-hidden="true"><rect x="3" y="0.5" width="6" height="11" rx="1" fill="none" stroke="var(--accent)" stroke-width="1.2"/><circle cx="6" cy="9.6" r="0.7" fill="var(--accent)"/></svg>
        <span>1 868 5550147</span>
      </p>
      <p class="contact__row">
        <svg viewBox="0 0 12 12" aria-hidden="true"><rect x="0.5" y="2.5" width="11" height="7.5" fill="var(--accent)"/><path d="M0.5 2.5 L6 7 L11.5 2.5" fill="none" stroke="var(--card)" stroke-width="1"/></svg>
        <span>m.tosh@ruvpartnersinc.example</span>
      </p>
      <p class="contact__row">
        <svg viewBox="0 0 12 12" aria-hidden="true"><circle cx="6" cy="6" r="5.5" fill="var(--accent)"/><path d="M0.5 6 H11.5 M6 0.5 C3 3.5 3 8.5 6 11.5 M6 0.5 C9 3.5 9 8.5 6 11.5" fill="none" stroke="var(--card)" stroke-width="0.8"/></svg>
        <span>ruvpartnersinc.example</span>
      </p>
    </div>
  </section>

  <section class="card card--back">
    <div class="brand-row">
      <div class="brand-mark">
        <div class="brand-mark__circle"></div>
        <div class="brand-mark__name">BOREAL<br>SUPPLIES</div>
      </div>
      <div class="company-mark company-mark--silver" style="position:static">
        <div class="company-mark__square"></div>
        <div class="company-mark__name">RUV Partners<br>Inc.</div>
      </div>
    </div>
    <p class="website">www.ruvpartnersinc.example</p>
  </section>
</body>
</html>
```